Cobbleway Restaurnt Lunch Menu Redesign:

We have two lunch special menus that need to be reformatted into a 4.25inx11in and need a graphics design update. Some menu items need to change and some descriptions need to updated. This new menu should double sided with the Main Dining Lunch Menu on the front side and Teppanyaki Lunch menu on the back.

Both menus should follow the same design formatting as the main dining lunch menu (font, sizing, ect.)

```html
<!DOCTYPE html>
<html lang="en">
<head>
<meta charset="utf-8">
<title>Cobbleway Restaurnt – Lunch Menu</title>
<link rel="stylesheet" href="https://fonts.googleapis.com/css2?family=Playfair+Display:ital,wght@0,400;0,700;1,400;1,700&family=Poppins:wght@400;500;600&family=Lora:ital,wght@1,400;1,600&display=swap">
<style>
  :root{
    --backdrop:#282828;
    --frame:#740505;
    --paper:#ffffff;
    --ink:#1f2b4d;
    --accent:#c13a3c;
    --blossom-a:#f3cfcf;
    --blossom-b:#c9a08f;
  }
  *{margin:0;padding:0;box-sizing:border-box}
  html,body{width:1076px;height:1200px;overflow:hidden;background:var(--backdrop)}
  .canvas{position:relative;width:1076px;height:1200px}
  .menu-card{position:absolute;top:96px;width:377px;height:974px;background:var(--frame)}
  .menu-card--front{left:126px}
  .menu-card--back{left:555px}
  .menu-card__paper{position:absolute;left:19px;top:20px;width:338px;height:935px;background:var(--paper)}
  .abs{position:absolute;left:0;width:100%;text-align:center;color:var(--ink)}
  .serif{font-family:"Playfair Display",serif}
  .italic{font-family:"Lora",serif;font-style:italic}
  .brand-name{font-family:"Playfair Display",serif;font-weight:400;font-size:27px;line-height:34px}
  .section-title{font-family:"Playfair Display",serif;font-size:22px;line-height:26px;font-weight:400}
  .lead{font-family:"Playfair Display",serif;font-style:italic;font-weight:700;font-size:11px;line-height:14px}
  .note{font-family:"Lora",serif;font-style:italic;font-size:8.5px;line-height:11px}
  .note--accent{color:var(--accent)}
  .divider{position:absolute;left:119px;width:100px;height:5px}
  .items{position:absolute;list-style:none;color:var(--ink)}
  .item{display:flex;justify-content:space-between;align-items:flex-start}
  .item__name{font-family:"Poppins",sans-serif;font-size:12px}
  .item__desc{font-family:"Lora",serif;font-style:italic;font-size:9px}
  .item__price{font-family:"Poppins",sans-serif;font-weight:600;font-size:9px}
  .front-items{left:26px;width:283px}
  .sandwich .item{height:35px}
  .sandwich .item__text{display:flex;flex-direction:column}
  .sandwich .item__name{line-height:14px}
  .sandwich .item__desc{line-height:12px}
  .sandwich .item__price{line-height:12px;margin-top:14px}
  .sushi-grid{position:absolute;left:26px;width:290px;display:grid;grid-template-columns:169px 1fr;grid-auto-flow:column;grid-template-rows:repeat(7,18.5px);list-style:none;color:var(--ink)}
  .sushi-grid li{line-height:18.5px;white-space:nowrap}
  .sushi-grid .item__desc{font-size:9px}
  .mains .item{height:22.2px;line-height:22.2px;align-items:center}
  .mains .item--detailed{height:31px;line-height:14px;align-items:flex-start}
  .mains .item--detailed .item__desc{display:block;line-height:14px}
  .back-items{left:43px;width:284px}
  .back-items .item{height:22.16px;line-height:22.16px;align-items:center}
  .special .item__name{font-weight:500}
  .blossom{position:absolute;left:60px;top:761px;width:278px;height:174px;background:radial-gradient(ellipse at 55% 60%,var(--blossom-a) 0%,rgba(243,207,207,.5) 55%,rgba(255,255,255,0) 75%)}
</style>
</head>
<body>
<div class="canvas">

  <section class="menu-card menu-card--front">
    <div class="menu-card__paper">
      <div class="abs brand-name" style="top:36px">Cobbleway Restaurnt</div>
      <div class="abs serif" style="top:84px;font-size:21px;font-weight:700;font-style:italic;line-height:26px">Lunch Specials</div>
      <div class="abs serif" style="top:111px;font-size:12px;font-style:italic;line-height:16px">Served Daily 11AM - 3PM</div>
      <svg class="divider" style="top:136px" viewBox="0 0 100 5"><path d="M0 0.5 Q50 2.5 100 0.5 L100 1.5 Q50 4 0 1.5Z" fill="var(--accent)"/><rect x="32" y="3.8" width="36" height="0.8" fill="var(--accent)"/></svg>

      <h2 class="abs section-title" style="top:149px">Sandwiches</h2>
      <div class="abs note" style="top:176px">Served with Choice of Miso Soup or House Salad &amp; Potato Chips</div>
      <ul class="items front-items sandwich" style="top:206px">
        <li class="item"><div class="item__text"><span class="item__name">Fried Breaded Calamari Steak</span><span class="item__desc">with Tomato, Lettuce &amp; Onion</span></div><span class="item__price">$16</span></li>
        <li class="item"><div class="item__text"><span class="item__name">Grilled Chicken</span><span class="item__desc">with Bacon, Tomato, Lettuce &amp; Mayonnaise Drizzle</span></div><span class="item__price">$16</span></li>
        <li class="item"><div class="item__text"><span class="item__name">Hamburger</span><span class="item__desc">with Lettuce, Tomato, Onion, Mayonnaise Drizzle</span></div><span class="item__price">$18</span></li>
        <li class="item"><div class="item__text"><span class="item__name">Fried Soft Shell Crab Burger</span><span class="item__desc">with Avocado, Lettuce, Tomato, Onion &amp; Mayo</span></div><span class="item__price">$20</span></li>
      </ul>
      <svg class="divider" style="top:346px" viewBox="0 0 100 5"><path d="M0 0.5 Q50 2.5 100 0.5 L100 1.5 Q50 4 0 1.5Z" fill="var(--accent)"/><rect x="32" y="3.8" width="36" height="0.8" fill="var(--accent)"/></svg>

      <h2 class="abs section-title" style="top:361px">Sushi Specials</h2>
      <div class="abs lead" style="top:390px">Please Select 4 of the followings for $16</div>
      <div class="abs note" style="top:406px">Served with a 4 piece California Roll &amp; Miso Soup or House Salad</div>
      <ul class="sushi-grid" style="top:430px">
        <li><span class="item__name">Hamach - </span><span class="item__desc">Yellowtail Tuna</span></li>
        <li><span class="item__name">Hotate - </span><span class="item__desc">Scallop</span></li>
        <li><span class="item__name">Ika - </span><span class="item__desc">Squid</span></li>
        <li><span class="item__name">Ikura - </span><span class="item__desc">Salmon Roe</span></li>
        <li><span class="item__name">Saba - </span><span class="item__desc">Mackerel</span></li>
        <li><span class="item__name">Sake - </span><span class="item__desc">Salmon</span></li>
        <li><span class="item__name">Tai - </span><span class="item__desc">Red Snapper</span></li>
        <li><span class="item__name">Maguro - </span><span class="item__desc">Yellow fin Tuna</span></li>
        <li><span class="item__name">Smoked Salmon</span></li>
        <li><span class="item__name">Tako - </span><span class="item__desc">Octopus</span></li>
        <li><span class="item__name">Unagi - </span><span class="item__desc">Salmon Roe</span></li>
        <li><span class="item__name">Ebi - </span><span class="item__desc">Shrimp</span></li>
        <li><span class="item__name">Tamago - </span><span class="item__desc">Egg</span></li>
      </ul>
      <svg class="divider" style="top:568px" viewBox="0 0 100 5"><path d="M0 0.5 Q50 2.5 100 0.5 L100 1.5 Q50 4 0 1.5Z" fill="var(--accent)"/><rect x="32" y="3.8" width="36" height="0.8" fill="var(--accent)"/></svg>

      <h2 class="abs section-title" style="top:582px">Main Courses</h2>
      <div class="abs lead" style="top:610px">Served with Rice &amp; Choice of Miso Soup or House Salad</div>
      <div class="abs note note--accent" style="top:627px">All Meals Served with Rice. Upgrade to fried rice for only $4</div>
      <ul class="items front-items mains" style="top:651px">
        <li class="item item--detailed"><div><span class="item__name">Fried Breaded Calamari Steak</span><span class="item__desc">Served Grilled or Tempura Fried</span></div><span class="item__price">$14</span></li>
        <li class="item"><span class="item__name">Chicken Teriyaki</span><span class="item__price">$16</span></li>
        <li class="item"><span class="item__name">Spicy Chicken Teriyaki</span><span class="item__price">$16</span></li>
        <li class="item"><span class="item__name">Beef Teriyaki</span><span class="item__price">$16</span></li>
        <li class="item"><span class="item__name">Spicy Beef Teriyaki</span><span class="item__price">$16</span></li>
        <li class="item"><span class="item__name">Chicken Katsu - <span class="item__desc">Breaded Chicken Breast</span></span><span class="item__price">$15</span></li>
        <li class="item"><span class="item__name">Katsu Don - <span class="item__desc">Fried Chicken Breast, Egg &amp; Onion over Rice</span></span><span class="item__price">$16</span></li>
        <li class="item"><span class="item__name">Unagi Don - <span class="item__desc">BBQ Eel over Rice</span></span><span class="item__price">$19</span></li>
        <li class="item"><span class="item__name">Shrimp &amp; Vegetable Tempura</span><span class="item__price">$16</span></li>
      </ul>
      <svg class="divider" style="top:869px" viewBox="0 0 100 5"><path d="M0 0.5 Q50 2.5 100 0.5 L100 1.5 Q50 4 0 1.5Z" fill="var(--accent)"/><rect x="32" y="3.8" width="36" height="0.8" fill="var(--accent)"/></svg>

      <div class="abs serif" style="top:881px;font-size:11px;line-height:14px">*Served Raw</div>
      <div class="abs note" style="top:894px;font-size:8px;line-height:10px">20% gratuity added to parties of 6 or more.</div>
      <div class="abs note" style="top:904px;font-size:8px;line-height:10px">Consuming raw or undercooked food may increase your risk of foodborne illness</div>
    </div>
  </section>

  <section class="menu-card menu-card--back">
    <div class="menu-card__paper">
      <h1 class="abs serif" style="top:27px;font-size:28px;font-weight:400;letter-spacing:1px;line-height:32px">TEPPANYAKI LUNCH</h1>
      <div class="abs serif" style="top:76px;font-size:18px;font-weight:700;line-height:24px">Available until 11-2:30pm</div>
      <div class="abs note" style="top:101px;font-size:9.5px;line-height:12px">Served with Miso Soup or Salad, Choice of Rice &amp; Vegetables</div>
      <svg class="divider" style="top:132px" viewBox="0 0 100 5"><path d="M0 0.5 Q50 2.5 100 0.5 L100 1.5 Q50 4 0 1.5Z" fill="var(--accent)"/><rect x="32" y="3.8" width="36" height="0.8" fill="var(--accent)"/></svg>

      <ul class="items back-items" style="top:153px">
        <li class="item"><span class="item__name">Hibachi Chicken</span><span class="item__price">$18</span></li>
        <li class="item"><span class="item__name">Hibachi Shrimp</span><span class="item__price">$19</span></li>
        <li class="item"><span class="item__name">Hibachi New York Steak</span><span class="item__price">$20</span></li>
        <li class="item"><span class="item__name">Hibachi Salmon</span><span class="item__price">$20</span></li>
        <li class="item"><span class="item__name">Teriyaki Beef</span><span class="item__price">$19</span></li>
        <li class="item"><span class="item__name">Hibachi Scallop</span><span class="item__price">$20</span></li>
        <li class="item"><span class="item__name">Chicken and Shrimp</span><span class="item__price">$21</span></li>
        <li class="item"><span class="item__name">Scallop and Shrimp</span><span class="item__price">$22</span></li>
        <li class="item"><span class="item__name">New York Steak and Chicken</span><span class="item__price">$22</span></li>
        <li class="item"><span class="item__name">New York Steak and Shrimp</span><span class="item__price">$23</span></li>
        <li class="item"><span class="item__name">New York Steak and Scallop</span><span class="item__price">$24</span></li>
        <li class="item"><span class="item__name">Filet Mignon</span><span class="item__price">$23</span></li>
        <li class="item"><span class="item__name">Filet Mignon and Chicken</span><span class="item__price">$25</span></li>
        <li class="item"><span class="item__name">Filet Mignon and Shrimp</span><span class="item__price">$26</span></li>
        <li class="item"><span class="item__name">Filet Mignon and Scallop</span><span class="item__price">$27</span></li>
      </ul>
      <svg class="divider" style="top:509px" viewBox="0 0 100 5"><path d="M0 0.5 Q50 2.5 100 0.5 L100 1.5 Q50 4 0 1.5Z" fill="var(--accent)"/><rect x="32" y="3.8" width="36" height="0.8" fill="var(--accent)"/></svg>

      <h2 class="abs section-title" style="top:529px">Special Menu</h2>
      <div class="abs italic" style="top:557px;font-size:10.5px;line-height:13px">Ages 12 and Under ~ Ages 65 and Older</div>
      <div class="abs italic" style="top:571px;font-size:10.5px;line-height:13px">Served with Miso Soup or Salad, Choice of Rice &amp; Vegetables</div>
      <ul class="items back-items special" style="top:613px">
        <li class="item"><span class="item__name">Hibachi Chicken</span><span class="item__price">$15</span></li>
        <li class="item"><span class="item__name">Hibachi Shrimp</span><span class="item__price">$16</span></li>
        <li class="item"><span class="item__name">Hibachi Scallop</span><span class="item__price">$18</span></li>
        <li class="item"><span class="item__name">Hibachi New York Steak</span><span class="item__price">$18</span></li>
        <li class="item"><span class="item__name">Hibachi Scallop</span><span class="item__price">$16</span></li>
        <li class="item"><span class="item__name">Teriyaki Beef</span><span class="item__price">$16</span></li>
      </ul>
      <div class="blossom" role="img" aria-label="Watercolour cherry blossom branch with red and pink flowers"></div>
    </div>
  </section>

</div>
</body>
</html>
```